BRAMBLE CABS

Taxi card design

Need changes very slow in replying to my messages.

Target Market(s)

Customers

Industry/Entity Type

Taxi

Contact Information for Business Card

See previous design

Font styles to use
Sans Serif

Colors
A7469A
B969AE
D3A5CF
EDDBEB
F8F0F9
6B429C
8869AF
B7A5CE
E3DAEB
F3F0F8

Requirements
Nice to have
• We are in the business of looking after people, not just driving vehicles front
Should not have
• Front number 01832 419 526 needs to big big

```html
<!DOCTYPE html>
<html lang="en">
<head>
<meta charset="utf-8">
<title>Bramble Cabs – Business Card</title>
<link rel="stylesheet" href="https://fonts.googleapis.com/css2?family=Exo+2:wght@500;600;700&family=Montserrat:wght@400;500&display=swap">
<style>
  :root {
    --plum: #A7469A;
    --plum-light: #B969AE;
    --violet: #6B429C;
    --violet-mid: #8869AF;
    --ink: #2a2a2a;
    --card-black: #1c1c1c;
    --card-grey: #3c3c3c;
    --paper: #ffffff;
    --backdrop: #dedede;
  }
  * { margin: 0; padding: 0; box-sizing: border-box; }
  html, body { width: 1200px; height: 1200px; overflow: hidden; background: var(--backdrop); }
  .canvas { position: relative; width: 1200px; height: 1200px; }

  .card {
    position: absolute; left: 255px; width: 690px; height: 392px;
    border-radius: 26px; overflow: hidden;
  }
  .card-front { top: 165px; background: var(--paper); }
  .card-back {
    top: 653px;
    background: linear-gradient(200deg, var(--card-grey) 0%, var(--card-black) 70%);
  }

  .phone-pill {
    position: absolute; display: flex; align-items: center; gap: 8px;
    height: 38px; width: 273px; border-radius: 19px; padding: 0 4px;
    font-family: "Exo 2", sans-serif; font-weight: 700; font-size: 30px;
    color: var(--paper); letter-spacing: 0.5px;
  }
  .phone-pill .icon { width: 30px; height: 30px; flex: none; }
  .card-front .phone-pill { left: 27px; top: 31px; background: var(--ink); }
  .card-back .phone-pill {
    left: 209px; top: 308px;
    background: linear-gradient(90deg, var(--violet), var(--plum));
  }

  .alt-numbers {
    position: absolute; left: 31px; top: 86px;
    font-family: "Exo 2", sans-serif; font-weight: 600; font-size: 20px;
    line-height: 20px; color: var(--plum); list-style: none;
  }
  .services {
    position: absolute; right: 40px; top: 33px; text-align: right;
    font-family: "Exo 2", sans-serif; font-weight: 600; font-size: 25px;
    line-height: 25px; color: var(--plum-light); list-style: none; letter-spacing: 0.5px;
  }

  .band { position: absolute; left: 0; top: 0; width: 690px; height: 392px; }

  .address {
    position: absolute; right: 381px; top: 270px; text-align: right;
    font-family: "Montserrat", sans-serif; font-size: 16px; line-height: 21px;
    color: var(--paper); font-style: normal;
  }
  .contacts {
    position: absolute; left: 335px; top: 270px; list-style: none;
    font-family: "Montserrat", sans-serif; font-size: 16px; line-height: 21px; color: var(--paper);
  }
  .contacts li { display: flex; align-items: center; gap: 9px; }
  .contacts svg { width: 12px; height: 12px; flex: none; }

  .brand {
    position: absolute; left: 0; right: 0; top: 150px;
    display: flex; justify-content: center; align-items: center; gap: 16px;
  }
  .brand-dot { width: 26px; height: 26px; border-radius: 50%; background: var(--plum); }
  .brand-name {
    font-family: "Exo 2", sans-serif; font-weight: 700; font-size: 60px;
    color: var(--paper); letter-spacing: 1px;
  }
</style>
</head>
<body>
<div class="canvas">

  <section class="card card-front">
    <svg class="band" viewBox="0 0 690 392" aria-hidden="true">
      <defs>
        <linearGradient id="bandFill" x1="0" y1="1" x2="1" y2="0">
          <stop offset="0" stop-color="#6B429C"/>
          <stop offset="0.5" stop-color="#A7469A"/>
          <stop offset="1" stop-color="#8869AF"/>
        </linearGradient>
      </defs>
      <path d="M0 240 C120 220 230 190 345 200 C460 210 570 225 690 235 L690 392 L0 392 Z" fill="#B969AE"/>
      <path d="M0 252 C120 232 230 204 345 214 C460 224 570 238 690 248 L690 392 L0 392 Z" fill="url(#bandFill)"/>
    </svg>

    <div class="phone-pill">
      <svg class="icon" viewBox="0 0 30 30" aria-hidden="true">
        <circle cx="15" cy="15" r="14" fill="#fff"/>
        <path d="M10 8 l3 0 l1.5 4 l-2 1.5 c1 2 2.5 3.5 4 4 l1.5 -2 l4 1.5 l0 3 c-7 1 -13 -5 -12 -12 z" fill="#A7469A"/>
      </svg>
      <span>01832 419 526</span>
    </div>

    <ul class="alt-numbers">
      <li>01832 41 55 55</li>
      <li>01832 30 30 30</li>
      <li>01832 41 77 22</li>
    </ul>

    <ul class="services">
      <li>AIRPORT TRANSFERS</li>
      <li>SCHOOL TRANSPORT</li>
      <li>MINIBUSES</li>
    </ul>

    <address class="address">
      Holly Lane Old Hall<br>
      Mill Row, Oundle<br>
      PE8 4QX
    </address>

    <ul class="contacts">
      <li>
        <svg viewBox="0 0 12 12" aria-hidden="true"><path d="M2 1 h2.5 l1 3 l-1.5 1 c.7 1.3 1.7 2.3 3 3 l1 -1.5 l3 1 v2.5 c-5 .5 -9.5 -4 -9 -9 z" fill="#fff"/></svg>
        Free Ph: 0800 555 0 319
      </li>
      <li>
        <svg viewBox="0 0 12 12" aria-hidden="true"><rect x="1" y="2.5" width="10" height="7" fill="#fff"/><path d="M1 2.5 l5 4 l5 -4" stroke="#8a4aa0" stroke-width="1" fill="none"/></svg>
        hello@bramblecabs.co.uk
      </li>
      <li>
        <svg viewBox="0 0 12 12" aria-hidden="true"><circle cx="6" cy="6" r="5.5" fill="#fff"/><path d="M3 4 q2 -1 3 1 q-1 2 1 3 M7 2 q1 1 3 1" stroke="#8a4aa0" stroke-width="1.2" fill="none"/></svg>
        www.bramblecabs.co.uk
      </li>
    </ul>
  </section>

  <section class="card card-back">
    <div class="brand">
      <span class="brand-dot"></span>
      <span class="brand-name">Bramble Cabs</span>
    </div>

    <div class="phone-pill">
      <svg class="icon" viewBox="0 0 30 30" aria-hidden="true">
        <circle cx="15" cy="15" r="14" fill="#fff"/>
        <path d="M10 8 l3 0 l1.5 4 l-2 1.5 c1 2 2.5 3.5 4 4 l1.5 -2 l4 1.5 l0 3 c-7 1 -13 -5 -12 -12 z" fill="#1c1c1c"/>
      </svg>
      <span>01832 419 526</span>
    </div>
  </section>

</div>
</body>
</html>
```